Simple, Professional and neat business card design for Vendralo Inc.

We're looking to re-vamp our business card design. We're a supplier of innovative feed ingredients for the North American animal agriculture industry. We are located in Lucknow, Ontario, Canada and our flagship product is a product that prevents milk fever in dairy cows when the calve, it is fed before calving and is very effective compared to other alternatives available on the market today.

Our company has Danish roots and we import all of our product from our Danish partner/manufacturer in Denmark. We like our design to embrace high professionalism while remaining neat and simple.

Target Market(s)

B2B, Feed Mills, Veterinary Clinics, Large integrators/producers,

Industry/Entity Type

Agribusiness

Contact Information for Business Card

We like the rounded corners because they make the card easy to sit in a wallet and not many use it so it makes the card stand out, just possibly something to take account for during the design.

As you can also see on the sliders below, looking for a that simple but proffesional scandinavian design.

Requirements
Nice to have
• Rounded corners
Should not have
• Too vibrant

```html
<!DOCTYPE html>
<html lang="en">
<head>
<meta charset="utf-8">
<title>Vendralo Inc. – Business Card</title>
<link rel="stylesheet" href="https://fonts.googleapis.com/css2?family=Montserrat:wght@700;800&family=Arimo:wght@400;700&display=swap">
<style>
  :root {
    --brand-blue: #0b5aa6;
    --card-white: #ffffff;
    --ink: #1c1c1c;
    --stage: #2a2a2a;
    --mark-gold: #d9c190;
  }
  * { box-sizing: border-box; margin: 0; padding: 0; }
  html, body { width: 1200px; height: 880px; overflow: hidden; }
  body {
    background: var(--stage);
    display: flex; flex-direction: column; align-items: center; justify-content: center;
    gap: 56px;
    font-family: "Arimo", Arial, sans-serif;
  }
  .card {
    width: 630px; height: 360px;
    border-radius: 26px;
    position: relative; overflow: hidden;
  }
  .brand-mark {
    width: 74px; height: 74px; border-radius: 50%;
    background: var(--mark-gold);
    flex: none;
  }
  .wordmark {
    font-family: "Montserrat", Arial, sans-serif;
    font-weight: 800; letter-spacing: 0.5px;
    text-transform: uppercase;
    white-space: nowrap;
  }

  /* Front */
  .card--front { background: var(--brand-blue); display: flex; align-items: center; justify-content: center; gap: 28px; }
  .card--front .wordmark { color: var(--card-white); font-size: 50px; }

  /* Back */
  .card--back { background: var(--card-white); }
  .back-brand { position: absolute; left: 44px; top: 34px; display: flex; align-items: center; gap: 26px; }
  .back-brand .wordmark { color: var(--brand-blue); font-size: 50px; }
  .person-name {
    position: absolute; left: 44px; top: 134px;
    font-weight: 700; font-size: 24px; line-height: 28px; color: var(--brand-blue);
  }
  .rule {
    position: absolute; left: 44px; right: 40px; top: 168px;
    height: 2px; background: var(--brand-blue);
  }
  .contact-lines {
    position: absolute; left: 44px; top: 180px;
    list-style: none; font-size: 17px; line-height: 23px; color: var(--ink);
  }
  .contact-lines b { font-weight: 700; }
  .online { position: absolute; right: 40px; top: 182px; text-align: right; }
  .social { display: flex; justify-content: flex-end; align-items: center; gap: 8px; margin-bottom: 6px;
    font-size: 14px; font-weight: 700; color: var(--brand-blue); }
  .social-dot { width: 18px; height: 18px; border-radius: 50%; background: var(--brand-blue); }
  .online p { font-size: 16px; line-height: 21px; color: var(--ink); }
  .online .web b { font-weight: 700; }
  .address-band {
    position: absolute; left: 0; right: 0; bottom: 0; height: 40px;
    background: var(--brand-blue);
    color: var(--card-white);
    font-size: 16px; letter-spacing: 3px;
    display: flex; align-items: center; justify-content: center;
  }
</style>
</head>
<body>
  <section class="card card--front" aria-label="Card front">
    <div class="brand-mark" aria-hidden="true"></div>
    <span class="wordmark">Vendralo Inc.</span>
  </section>

  <section class="card card--back" aria-label="Card back">
    <div class="back-brand">
      <div class="brand-mark" aria-hidden="true"></div>
      <span class="wordmark">Vendralo Inc.</span>
    </div>
    <h2 class="person-name">Mikkel Sorensen</h2>
    <div class="rule"></div>
    <ul class="contact-lines">
      <li><b>Mobile:</b> 519-555-0148</li>
      <li><b>Office:</b> 519-555-0172</li>
      <li><b>Toll Free:</b> 888-555-0190</li>
      <li><b>Fax:</b> 519-555-0163</li>
    </ul>
    <div class="online">
      <div class="social"><span class="social-dot" aria-hidden="true"></span>vendralo</div>
      <p class="email">mikkel@vendralo.com</p>
      <p class="web">www.<b>vendralo</b>.com</p>
    </div>
    <div class="address-band">Box 412, Fernhill, Ontario Canada N0A 3K0</div>
  </section>
</body>
</html>
```